SUMMIT GATHERING 2021. August 20th -22nd.

The Hosts of the conference: Grace Tabernacle-Pastors Ron n Della ( Picture with two persons)

Guest Minister: Bishop Lucinda Okotieno. (Cedar Ridge Awakening)

Venue:
Sealand Gateway Lodgeview. 4817 North 239th Avenue Seattle, WA 98174.

Conference times.
Friday August 20th 6pm-8:30pm
Saturday August 21st. 6pm-8:30pm

Sunday August 22nd 10am-1pm
“ CHURCH RENEWAL GATHERING”

5pm-7:30pm
TWOFOLD SURGE GATHERING.

Target Market(s)

18-55

Industry/Entity Type

Religious/ Entertainment.

Requirements
Must have
• A highlight of the Relaunch service on Sunday August 22nd 5pm-7:30pm.
Nice to have
• Excellent ideas….

```html
<!DOCTYPE html>
<html lang="en">
<head>
<meta charset="utf-8">
<title>Summit Gathering 2021</title>
<link href="https://fonts.googleapis.com/css2?family=Josefin+Sans:wght@300;400;600;700&display=swap" rel="stylesheet">
<style>
  :root {
    --ink: #0b0b0b;
    --paper: #ffffff;
    --gold: #b39461;
    --gold-light: #f1e6c4;
    --gold-dark: #6e4e2c;
    --rule: #8a6e47;
  }
  * { margin: 0; padding: 0; box-sizing: border-box; }
  html, body { width: 925px; height: 1200px; overflow: hidden; background: var(--ink); }
  .poster {
    position: relative; width: 925px; height: 1200px; overflow: hidden;
    background: linear-gradient(160deg, #141414 0%, #0a0a0a 55%, #0e0e0e 100%);
    font-family: "Josefin Sans", sans-serif; color: var(--paper);
  }
  .art { position: absolute; inset: 0; }
  .abs { position: absolute; }
  .center { text-align: center; }

  .brand {
    left: 392px; top: 62px; width: 141px; height: 90px;
    display: flex; flex-direction: column; align-items: center; justify-content: center; gap: 10px;
    color: var(--gold); font-weight: 600; font-size: 13px; letter-spacing: 2px;
  }
  .brand-mark { width: 40px; height: 40px; border: 2px solid var(--gold); }

  .title {
    left: 0; width: 925px; top: 178px;
    font-size: 64px; font-weight: 600; letter-spacing: 2px; line-height: 1;
    background: linear-gradient(180deg, #fff7e2 0%, #d4bc8a 55%, #8d7048 100%);
    -webkit-background-clip: text; background-clip: text; color: transparent;
  }
  .subtitle {
    left: 0; width: 925px; top: 250px;
    font-size: 32px; font-weight: 400; letter-spacing: 19px; text-indent: 19px; line-height: 1;
    color: #d8c69d;
  }
  .year { left: 0; width: 925px; top: 288px; font-size: 32px; font-weight: 300; line-height: 1; }
  .dates { left: 0; width: 925px; top: 334px; font-size: 11px; font-weight: 600; letter-spacing: 7px; text-indent: 7px; }

  .photo {
    position: absolute; border-radius: 50%;
  }
  .photo-hosts { left: 185px; top: 430px; width: 134px; height: 127px;
    background: radial-gradient(circle at 60% 40%, #c23dbf 0%, #5a2a6a 45%, #3a2a22 100%); }
  .photo-guest { left: 185px; top: 670px; width: 134px; height: 127px;
    background: radial-gradient(circle at 50% 45%, #5b4033 0%, #8a8a86 55%, #dcdedd 100%); }

  .role { font-size: 13px; font-weight: 300; letter-spacing: 0.3px; }
  .name {
    font-size: 21px; font-weight: 700; letter-spacing: 0.3px;
    background: linear-gradient(180deg, #fff3d6 0%, #c9aa74 100%);
    -webkit-background-clip: text; background-clip: text; color: transparent;
  }
  .affil { font-size: 12px; font-weight: 300; }

  .venue { left: 312px; width: 556px; top: 900px; font-size: 13.5px; font-weight: 600; }
  .times { left: 392px; width: 400px; top: 957px; font-size: 11.5px; font-weight: 300; line-height: 17px; }
  .times-head { color: var(--gold); font-weight: 400; }
  .service { width: 260px; top: 1055px; font-size: 11.5px; font-weight: 300; line-height: 17px; }
  .service-head { color: var(--gold); font-weight: 600; font-size: 12.5px; }
  .service-morning { left: 292px; }
  .service-evening { left: 631px; }
</style>
</head>
<body>
<main class="poster">
  <svg class="art" width="925" height="1200" viewBox="0 0 925 1200" aria-hidden="true">
    <defs>
      <linearGradient id="gold-bar" x1="0" y1="0" x2="0" y2="1">
        <stop offset="0" stop-color="#8c6c44"/>
        <stop offset="0.12" stop-color="#f5f6e6"/>
        <stop offset="0.35" stop-color="#e2d4a8"/>
        <stop offset="0.65" stop-color="#b39466"/>
        <stop offset="1" stop-color="#6e4b29"/>
      </linearGradient>
      <linearGradient id="gold-ring" x1="0" y1="0" x2="1" y2="1">
        <stop offset="0" stop-color="#8a6a3e"/>
        <stop offset="0.35" stop-color="#f4e5bc"/>
        <stop offset="0.7" stop-color="#b08a55"/>
        <stop offset="1" stop-color="#5e4224"/>
      </linearGradient>
      <linearGradient id="rule" x1="0" x2="1">
        <stop offset="0" stop-color="#6e5334"/>
        <stop offset="0.5" stop-color="#c7a878"/>
        <stop offset="1" stop-color="#6e5334"/>
      </linearGradient>
    </defs>
    <!-- top rules -->
    <rect x="32" y="22" width="264" height="3" fill="url(#rule)"/>
    <rect x="330" y="22" width="264" height="3" fill="url(#rule)"/>
    <rect x="628" y="22" width="264" height="3" fill="url(#rule)"/>
    <!-- year rules -->
    <line x1="297" y1="303" x2="399" y2="303" stroke="#fff" stroke-width="1.5"/>
    <line x1="526" y1="303" x2="629" y2="303" stroke="#fff" stroke-width="1.5"/>
    <!-- gold column -->
    <rect x="68" y="360" width="177" height="776" fill="url(#gold-bar)"/>
    <!-- portrait frames -->
    <ellipse cx="252" cy="493" rx="116" ry="110" fill="#0a0a0a"/>
    <ellipse cx="252" cy="493" rx="102" ry="97" fill="none" stroke="url(#gold-ring)" stroke-width="13"/>
    <ellipse cx="252" cy="733" rx="116" ry="110" fill="#0a0a0a"/>
    <ellipse cx="252" cy="733" rx="102" ry="97" fill="none" stroke="url(#gold-ring)" stroke-width="13"/>
    <!-- venue frame -->
    <path d="M537 863 H312 V937 H868 V863 H640" fill="none" stroke="var(--rule)" stroke-width="1.5"/>
    <circle cx="589" cy="860" r="27" fill="#a88a5c"/>
    <path d="M589 872 C583 864 580 860 580 855 A9 9 0 0 1 598 855 C598 860 595 864 589 872 Z" fill="#0b0b0b"/>
    <circle cx="589" cy="855" r="3" fill="#a88a5c"/>
    <!-- divider -->
    <line x1="589" y1="1022" x2="589" y2="1120" stroke="#fff" stroke-width="1.2" stroke-dasharray="5 4"/>
    <!-- bottom rule -->
    <rect x="32" y="1170" width="860" height="3" fill="url(#rule)"/>
  </svg>

  <div class="abs brand"><span class="brand-mark"></span><span>GRACE TABERNACLE</span></div>

  <h1 class="abs title center">SUMMIT</h1>
  <p class="abs subtitle center">GATHERING</p>
  <p class="abs year center">2021</p>
  <p class="abs dates center">AUGUST 20TH -22ND</p>

  <div class="photo photo-hosts" role="img" aria-label="Portrait of hosts Ron and Della"></div>
  <div class="photo photo-guest" role="img" aria-label="Portrait of guest minister Bishop Lucinda Okotieno"></div>

  <section class="abs" style="left:399px; top:452px;">
    <p class="role">HOSTS OF THE CONFERENCE</p>
    <p class="name" style="margin-top:16px;">RON N DELLA</p>
    <p class="affil" style="margin-top:4px;">(Grace Tabernacle-Pastors)</p>
  </section>

  <section class="abs" style="left:399px; top:692px;">
    <p class="role">GUEST MINISTER</p>
    <p class="name" style="margin-top:16px;">BISHOP LUCINDA OKOTIENO</p>
    <p class="affil" style="margin-top:4px;">(Cedar Ridge Awakening)</p>
  </section>

  <p class="abs venue center">Sealand Gateway Lodgeview. 4817 North 239th Avenue Seattle, WA 98174.</p>

  <div class="abs times center">
    <p class="times-head">Conference times.</p>
    <p>Friday August 20th 6pm-8:30pm</p>
    <p>Saturday August 21st. 6pm-8:30pm</p>
  </div>

  <div class="abs service service-morning center">
    <p class="service-head">CHURCH RENEWAL GATHERING</p>
    <p>Sunday August 22nd 10am-1pm</p>
  </div>
  <div class="abs service service-evening center">
    <p class="service-head">TWOFOLD SURGE GATHERING</p>
    <p>Sunday August 22nd 5pm-7:30pm</p>
  </div>
</main>
</body>
</html>
```